Professional and stylish textiles catalogue

Wool throws and cushions product catalogue.
Target audience are business customers (interior stores). Besides providing information about products the catalogue must able to sell, therefore we expect it to be professional and stylish.
Size A5 horizontal.
Content:
1. Cover: Logo and 2011/12 on front, company details on reverse;
2. Page with photo and short info about company;
3. Product pages spread - one item per page. Total 15 double-page spreads;
4. Info page with photo and small text about gift packaging.
Products - throws and cushions. Located as a pair on each spread: throw on the left, cushion on the right. One double-page spread with three throws.
Products mostly are in natural colours: grey, beige and brown. Three throws/cushions in light shades of rose, green and blue.
Comments: catalogue must be in bright colours, could be white with colourful details. Will be great if each product's double-page spread will have stylish details (could be lines) in colours of the product located in this certain double-page spread.
Materials provided:
1. Texts;
2. White background pictures of each product;
3. Several product pictures taken in the interior to use for the cover;
4. Logo.
Complete set of pictures in high resolution will be provided on request.
Business

```html
<!DOCTYPE html>
<html lang="en">
<head>
<meta charset="utf-8">
<title>Lanvere Collection 2011/12 – Catalogue Spreads</title>
<link href="https://fonts.googleapis.com/css2?family=Lato:wght@300;400;700&display=swap" rel="stylesheet">
<style>
  :root {
    --canvas: #ffffff;
    --page-edge: #e9e9e8;
    --page-light: #f7f7f6;
    --band-dark: #45454d;
    --band-mid: #5a5a62;
    --ink: #2b2b2b;
    --ink-soft: #4a4a4a;
    --white: #ffffff;
    --throw-tone-a: #c9b49a;
    --throw-tone-b: #6d5a4a;
    --cushion-tone-a: #9a9a9a;
    --cushion-tone-b: #7c7c7c;
    --box-tone-a: #b9b7b4;
    --box-tone-b: #e1dfdc;
  }
  * { margin: 0; padding: 0; box-sizing: border-box; }
  html, body { width: 1200px; height: 1016px; overflow: hidden; background: var(--canvas); }
  body { font-family: "Lato", sans-serif; color: var(--ink); position: relative; }

  .spread { position: absolute; left: 53px; width: 1075px; display: flex; box-shadow: 0 4px 6px rgba(0,0,0,0.12); }
  .spread--products { top: 91px; height: 364px; }
  .spread--closing { top: 549px; height: 365px; }

  .page { position: relative; width: 50%; height: 100%; }
  .page--left { background: linear-gradient(90deg, var(--page-edge) 0%, var(--page-light) 70%, #e6e6e5 100%); }
  .page--right { background: linear-gradient(90deg, #dededd 0%, var(--page-light) 25%, var(--page-edge) 100%); }

  .header-band { position: absolute; top: 0; left: 0; right: 0; height: 60px;
    background: linear-gradient(180deg, var(--band-dark), var(--band-mid)); }
  .brand { position: absolute; left: 27px; top: 31px; display: flex; align-items: center; gap: 7px;
    color: var(--white); font-size: 14px; letter-spacing: 0.5px; font-weight: 400; }
  .brand-square { width: 11px; height: 11px; background: var(--white); }
  .collection-tag { position: absolute; right: 25px; top: 29px; text-align: right; color: var(--white);
    font-size: 11.5px; line-height: 13px; font-weight: 400; letter-spacing: 0.3px; }

  .product-info { position: absolute; top: 147px; font-size: 9px; line-height: 11px; color: var(--ink-soft); }
  .product-info h2 { font-size: 13px; font-weight: 400; color: var(--ink); line-height: 14px; letter-spacing: 0.2px; }
  .product-info .size { margin-top: 10px; }
  .product-info--throw { left: 64px; }
  .product-info--cushion { left: 371px; }

  .product-photo { position: absolute; }
  .product-photo--throw { left: 219px; top: 86px; width: 193px; height: 190px;
    background: linear-gradient(90deg, var(--throw-tone-a) 0%, var(--throw-tone-a) 22%, var(--throw-tone-b) 40%, #5e4d40 100%); }
  .product-photo--cushion { left: 65px; top: 86px; width: 207px; height: 190px; border-radius: 6px;
    background: linear-gradient(135deg, var(--cushion-tone-a), var(--cushion-tone-b)); }

  .style-number { position: absolute; top: 326px; font-size: 7px; color: var(--ink-soft); }
  .style-number--throw { left: 340px; }
  .style-number--cushion { left: 133px; }
  .folio { position: absolute; font-size: 7px; color: var(--ink-soft); }
  .folio--4 { left: 25px; top: 332px; }
  .folio--5 { right: 25px; top: 332px; }
  .folio--34 { left: 25px; top: 332px; }

  .gift-photo { position: absolute; background: linear-gradient(180deg, var(--box-tone-a), var(--box-tone-b)); }
  .gift-photo--stacked { left: 367px; top: 33px; width: 160px; height: 73px; }
  .gift-photo--open-large { left: 27px; top: 123px; width: 170px; height: 200px; }
  .gift-photo--open-small { left: 207px; top: 173px; width: 125px; height: 136px; }

  .gift-note { position: absolute; left: 226px; top: 114px; width: 170px; font-size: 8px; line-height: 10.5px; color: var(--ink); }

  .company-details { position: absolute; left: 0; right: 0; top: 150px; text-align: center; font-style: normal;
    font-size: 11px; line-height: 13px; color: var(--ink-soft); font-weight: 300; }
  .company-details strong { font-weight: 700; color: var(--ink); }
</style>
</head>
<body>

<section class="spread spread--products">
  <div class="page page--left">
    <div class="header-band">
      <div class="brand"><span class="brand-square"></span><span>LANVERE</span></div>
    </div>
    <div class="product-info product-info--throw">
      <h2>MAYFIELD CHECK</h2>
      <p>Handwoven Throw</p>
      <p>100% baby alpaca</p>
      <p>Natural, undyed colours</p>
      <p class="size">Size 127 x 175 cm</p>
    </div>
    <div class="product-photo product-photo--throw" role="img" aria-label="Folded beige and brown alpaca throw with fringe"></div>
    <p class="style-number style-number--throw">Style nr. 0400312</p>
    <p class="folio folio--4">4</p>
  </div>
  <div class="page page--right">
    <div class="header-band">
      <div class="collection-tag">COLLECTION<br>2011/12</div>
    </div>
    <div class="product-photo product-photo--cushion" role="img" aria-label="Grey handwoven alpaca cushion"></div>
    <div class="product-info product-info--cushion">
      <h2>SLATE</h2>
      <p>Handwoven Cushion</p>
      <p>100% baby alpaca</p>
      <p>Natural, undyed colours</p>
      <p class="size">Size 127 x 175 cm</p>
    </div>
    <p class="style-number style-number--cushion">Style number 0500208</p>
    <p class="folio folio--5">5</p>
  </div>
</section>

<section class="spread spread--closing">
  <div class="page page--left">
    <div class="gift-photo gift-photo--stacked" role="img" aria-label="Two closed grey gift boxes stacked"></div>
    <p class="gift-note">Gift wrapped in delightful handmade boxes, Lanvere throws and cushions will be a handy addition to your current collection and are certain to please your valuable customers.</p>
    <div class="gift-photo gift-photo--open-large" role="img" aria-label="Open grey gift box holding a folded checked throw"></div>
    <div class="gift-photo gift-photo--open-small" role="img" aria-label="Open grey gift box holding a folded cushion"></div>
    <p class="folio folio--34">34</p>
  </div>
  <div class="page page--right">
    <address class="company-details">
      <strong>Lanvere Ltd</strong><br>
      28 Harrow Mews<br>
      London, N7 2QT<br>
      +44 (0) 7000 555 218<br>
      info@lanvere.co.uk
    </address>
  </div>
</section>

</body>
</html>
```